Design a CD Cover For Baby Music and Lullabies To Appear on Tunvale Store etc.

Please read this brief before you design. Otherwise you will be wasting your time.

I need a cd cover for music albums which will appear on streaming sites such as Tunvale Store Melodrift, Vimtro etc. for the brand Snug Cradle Tunes. The thumbnails are quite small so the text needs to be quite large.

I need a design if possible, in which I can simply alter the title of the album and the baby picture so that each album has a different cover but works with the branding.

You can check out the Snug Cradle Tunes on the Tunvale store.
https://play.melodriftaudio.net/artist/8kQ3xTnRwLpV27hYbMdZc4

I made those covers and I really don't like them at all! As you can tell I am not a graphic designer. Ha.

Please help me with a modern, eye catching and cute design that will work across the brand now and in the future. The SCT logo and the name Snug Cradle Tunes is the only thing that needs to be used somewhere in the design.

Please use the title

Gentle Static Hums For Nap Time Series A

for this first album.
(White noise sounds are hair dryers, vacuum cleaners, fans, wind, rain, the sea, white noise, pink noise, brown noise etc. )

Here is an example of album covers which are coherent. A style like this without the over the top text would be good. But don't copy these!
https://play.melodriftaudio.net/artist/9TqWmLx5Rb2Hn7KcVpYe1z

Target Market(s)

Parents of babies.

Font styles to use
Serif
Sans Serif

Colors

Designer to choose colors to be used in the design.

Requirements
Must have
• Large font so it can been seen in the melodrift thumbnail. A photo of a baby. Please take a look at the melodrift and tunvale stores. The Snug Cradle Tunes logo.
• Album Title
• Gentle Static Hums For Nap Time Series A

```html
<!DOCTYPE html>
<html lang="en">
<head>
<meta charset="utf-8">
<title>Gentle Static Hums For Nap Time – Series A</title>
<link rel="stylesheet" href="https://fonts.googleapis.com/css2?family=Amatic+SC:wght@400;700&display=swap">
<style>
  :root {
    --bg-top: #6f6a86;
    --bg-mid: #b89aa6;
    --bg-low: #8e6f78;
    --glow: #f3d9cf;
    --record-dark: #262326;
    --record-edge: #3a3539;
    --skin: #e9c2ac;
    --title-ink: #4b5060;
    --title-halo: rgba(255, 245, 240, 0.85);
    --badge: #2f8fd8;
  }
  html, body {
    margin: 0;
    padding: 0;
    width: 1200px;
    height: 1200px;
    overflow: hidden;
  }
  .cover {
    position: relative;
    width: 1200px;
    height: 1200px;
    overflow: hidden;
    background:
      radial-gradient(circle at 12% 22%, rgba(243, 217, 207, 0.55) 0 9%, transparent 10%),
      radial-gradient(circle at 88% 8%, rgba(243, 217, 207, 0.45) 0 7%, transparent 8%),
      radial-gradient(circle at 6% 60%, rgba(243, 217, 207, 0.4) 0 6%, transparent 7%),
      radial-gradient(circle at 95% 78%, rgba(243, 217, 207, 0.45) 0 8%, transparent 9%),
      radial-gradient(ellipse at 50% 40%, var(--bg-mid) 0%, var(--bg-top) 70%),
      linear-gradient(180deg, var(--bg-top) 0%, var(--bg-mid) 55%, var(--bg-low) 100%);
  }
  .background-photo {
    position: absolute;
    inset: 0;
  }
  .record-photo {
    position: absolute;
    left: 156px;
    top: 156px;
    width: 888px;
    height: 888px;
    border-radius: 50%;
    background:
      radial-gradient(ellipse 26% 42% at 52% 50%, var(--skin) 0 60%, transparent 62%),
      radial-gradient(circle at 50% 50%, #e8dcc2 0 24%, var(--record-dark) 25% 92%, var(--record-edge) 96%);
    box-shadow: 0 10px 40px rgba(40, 30, 40, 0.35);
  }
  .album-title {
    position: absolute;
    left: 0;
    right: 0;
    top: 680px;
    margin: 0;
    text-align: center;
    font-family: "Amatic SC", "Trebuchet MS", sans-serif;
    font-weight: 700;
    font-size: 158px;
    line-height: 150px;
    letter-spacing: 4px;
    color: var(--title-ink);
    -webkit-text-stroke: 0;
    text-shadow:
      0 0 3px var(--title-halo),
      0 0 6px var(--title-halo),
      2px 2px 0 var(--title-halo),
      -2px -2px 0 var(--title-halo),
      2px -2px 0 var(--title-halo),
      -2px 2px 0 var(--title-halo);
  }
  .album-title .line {
    display: block;
  }
  .series {
    position: absolute;
    top: 1036px;
    left: 278px;
    display: flex;
    align-items: center;
    gap: 28px;
  }
  .brand-mark {
    width: 126px;
    height: 126px;
    border-radius: 50%;
    background: var(--badge);
  }
  .series-label {
    font-family: "Amatic SC", "Trebuchet MS", sans-serif;
    font-weight: 700;
    font-size: 112px;
    line-height: 1;
    letter-spacing: 4px;
    color: var(--title-ink);
    text-shadow:
      0 0 3px var(--title-halo),
      2px 2px 0 var(--title-halo),
      -2px -2px 0 var(--title-halo),
      2px -2px 0 var(--title-halo),
      -2px 2px 0 var(--title-halo);
  }
</style>
</head>
<body>
  <main class="cover">
    <div class="background-photo" role="img" aria-label="Soft out-of-focus pink and mauve bokeh lights"></div>
    <div class="record-photo" role="img" aria-label="Photo of a sleeping baby with a floral headband curled on a vinyl record"></div>
    <h1 class="album-title">
      <span class="line">Gentle Static Hums</span>
      <span class="line">For Nap Time</span>
    </h1>
    <div class="series">
      <div class="brand-mark" role="img" aria-label="Snug Cradle Tunes"></div>
      <span class="series-label">Series A</span>
    </div>
  </main>
</body>
</html>
```